Flyer Design

I need a nice professional flyer design to use for advertising my lawn/snow removal business. Flyers I am using are 5.47"x4.21". I've attached a flyer I found online that I liked. Just wanting something creative and professional. The images of the logos I attached are of the original logo design, and the new color design we are using. There is also a mockup of our tshirt design to give you an idea of the actual color on the tshirt, since the jpeg logo isn't exactly accurate on color.
Things I need on the flyer in no particular order:
"Snow is coming"
"Don't Wait Until It's TOO LATE!"
"Free Estimates"
Services offered
"Commercial/Residential"
"Snow Plowing"
"Snow Blowing"
"Snow Shoveling"
"Ice Removal"
"Salting/Sanding"
"Fully Licensed and Insured"
"Available and ON CALL 24/7"
"Seasonal Packages Available"
"CALL NOW TO RESERVE"

```html
<!DOCTYPE html>
<html lang="en">
<head>
<meta charset="utf-8">
<title>Snow Is Coming – Brightline Lawn &amp; Landscape</title>
<link rel="stylesheet" href="https://fonts.googleapis.com/css2?family=Kaushan+Script&family=Open+Sans:wght@400;600&family=Ubuntu:wght@400;500;700&display=swap">
<style>
  :root {
    --red: #e3141b;
    --orange: #ef7a26;
    --orange-soft: #f6c49f;
    --ink: #111111;
    --slate: #4a4a48;
    --grey-text: #3d3d3d;
    --white: #ffffff;
  }
  * { margin: 0; padding: 0; box-sizing: border-box; }
  html, body { width: 1200px; height: 924px; overflow: hidden; background: var(--white); }
  .flyer { position: relative; width: 1200px; height: 924px; overflow: hidden; background: var(--white); font-family: "Ubuntu", sans-serif; }
  .flyer__art { position: absolute; inset: 0; }

  .brand { position: absolute; left: 150px; top: 84px; display: flex; align-items: center; gap: 12px; }
  .brand__dot { width: 28px; height: 28px; border-radius: 50%; background: var(--orange); flex: none; }
  .brand__name { font-family: "Ubuntu", sans-serif; font-weight: 700; font-size: 30px; color: var(--ink); }

  .badge { position: absolute; left: 168px; top: 480px; width: 180px; text-align: center; color: var(--white); font-family: "Open Sans", sans-serif; font-weight: 600; font-size: 26px; line-height: 1.35; }

  .headline { position: absolute; left: 380px; width: 420px; text-align: center; font-family: "Ubuntu", sans-serif; font-weight: 700; font-size: 108px; line-height: 1; color: var(--red); text-shadow: 4px 4px 4px rgba(0,0,0,0.35); letter-spacing: -1px; }
  .headline--top { top: 400px; }
  .headline--bottom { top: 512px; }

  .tagline { position: absolute; left: 300px; width: 514px; top: 644px; text-align: center; font-family: "Ubuntu", sans-serif; font-weight: 700; font-size: 32px; color: var(--ink); white-space: nowrap; }
  .tagline__alert { color: var(--red); }

  .packages { position: absolute; left: 300px; width: 480px; top: 708px; text-align: center; font-family: "Kaushan Script", "Brush Script MT", cursive; font-size: 40px; color: var(--ink); white-space: nowrap; }

  .services { position: absolute; left: 826px; top: 446px; }
  .services__title { font-family: "Ubuntu", sans-serif; font-weight: 700; font-size: 36px; color: var(--red); text-shadow: 2px 2px 3px rgba(0,0,0,0.3); margin-bottom: 14px; }
  .services__list { list-style: none; }
  .services__item { display: flex; align-items: center; gap: 10px; font-family: "Open Sans", sans-serif; font-size: 24px; color: var(--grey-text); height: 36.5px; }
  .services__bullet { width: 17px; height: 17px; border-radius: 50%; background: var(--orange); box-shadow: 0 0 0 2px var(--orange-soft); flex: none; }

  .credentials { position: absolute; left: 48px; top: 812px; color: var(--white); font-family: "Open Sans", sans-serif; }
  .credentials__line { font-size: 24px; }
  .credentials__hours { font-size: 36px; margin-top: 6px; }

  .reserve { position: absolute; left: 718px; top: 812px; font-family: "Ubuntu", sans-serif; font-weight: 700; font-size: 36px; color: var(--ink); line-height: 1.3; }
</style>
</head>
<body>
<main class="flyer">
  <svg class="flyer__art" width="1200" height="924" viewBox="0 0 1200 924">
    <defs>
      <clipPath id="sceneClip">
        <path d="M0 0 H1200 V200 C960 240 720 265 516 360 C336 444 216 564 144 720 H0 Z"/>
      </clipPath>
      <clipPath id="blowerClip">
        <circle cx="1014" cy="162" r="198"/>
      </clipPath>
      <linearGradient id="snowBase" x1="0" y1="0" x2="1" y2="1">
        <stop offset="0" stop-color="#9aa7b2"/>
        <stop offset="0.45" stop-color="#d9e0e6"/>
        <stop offset="1" stop-color="#b8c3cc"/>
      </linearGradient>
      <radialGradient id="workerGlow" cx="200" cy="300" r="170" gradientUnits="userSpaceOnUse">
        <stop offset="0" stop-color="#f05a1e" stop-opacity="0.85"/>
        <stop offset="0.5" stop-color="#f0803f" stop-opacity="0.4"/>
        <stop offset="1" stop-color="#f0803f" stop-opacity="0"/>
      </radialGradient>
      <radialGradient id="truckGlow" cx="560" cy="170" r="190" gradientUnits="userSpaceOnUse">
        <stop offset="0" stop-color="#b3262c" stop-opacity="0.85"/>
        <stop offset="0.45" stop-color="#8a4a52" stop-opacity="0.4"/>
        <stop offset="1" stop-color="#8a4a52" stop-opacity="0"/>
      </radialGradient>
      <radialGradient id="shadowGlow" cx="90" cy="180" r="220" gradientUnits="userSpaceOnUse">
        <stop offset="0" stop-color="#55606a" stop-opacity="0.6"/>
        <stop offset="1" stop-color="#55606a" stop-opacity="0"/>
      </radialGradient>
      <linearGradient id="blowerBase" x1="0" y1="0" x2="1" y2="1">
        <stop offset="0" stop-color="#7d8790"/>
        <stop offset="0.4" stop-color="#dfe5ea"/>
        <stop offset="1" stop-color="#f4f7f9"/>
      </linearGradient>
      <radialGradient id="blowerGlow" cx="1010" cy="200" r="110" gradientUnits="userSpaceOnUse">
        <stop offset="0" stop-color="#a3262c" stop-opacity="0.7"/>
        <stop offset="0.55" stop-color="#5b5f66" stop-opacity="0.35"/>
        <stop offset="1" stop-color="#5b5f66" stop-opacity="0"/>
      </radialGradient>
    </defs>

    <g role="img" aria-label="Photo of road crews in orange gear shoveling snow beside a red snowplow truck in a blizzard" clip-path="url(#sceneClip)">
      <rect x="0" y="0" width="1200" height="720" fill="url(#snowBase)"/>
      <rect x="0" y="0" width="1200" height="720" fill="url(#shadowGlow)"/>
      <rect x="0" y="0" width="1200" height="720" fill="url(#truckGlow)"/>
      <rect x="0" y="0" width="1200" height="720" fill="url(#workerGlow)"/>
    </g>
    <path d="M144 720 C216 564 336 444 516 360 C720 265 960 240 1200 200" fill="none" stroke="var(--red)" stroke-width="5"/>

    <g role="img" aria-label="Photo of a person clearing a snowy sidewalk with a red snow blower" clip-path="url(#blowerClip)">
      <rect x="816" y="-36" width="396" height="396" fill="url(#blowerBase)"/>
      <rect x="816" y="-36" width="396" height="396" fill="url(#blowerGlow)"/>
    </g>
    <circle cx="1014" cy="162" r="198" fill="none" stroke="var(--red)" stroke-width="8"/>

    <circle cx="258" cy="540" r="94" fill="var(--orange)"/>
    <circle cx="258" cy="540" r="80" fill="none" stroke="var(--white)" stroke-width="5"/>

    <rect x="0" y="782" width="1200" height="10" fill="var(--red)"/>
    <rect x="0" y="792" width="1200" height="132" fill="var(--orange)"/>
    <polygon points="0,792 555,792 600,858 555,924 0,924" fill="var(--slate)"/>
    <polygon points="555,792 585,792 630,858 585,924 555,924 600,858" fill="var(--white)"/>
  </svg>

  <div class="brand">
    <span class="brand__dot"></span>
    <span class="brand__name">Brightline Lawn &amp; Landscape</span>
  </div>

  <div class="badge">FREE<br>Estimates</div>

  <h1 class="headline headline--top">Snow is</h1>
  <p class="headline headline--bottom">coming</p>

  <p class="tagline">Don't Wait Until It's <span class="tagline__alert">TOO LATE</span></p>
  <p class="packages">Seasonal Packages Available</p>

  <section class="services">
    <h2 class="services__title">Services offered</h2>
    <ul class="services__list">
      <li class="services__item"><span class="services__bullet"></span>Commercial/Residential</li>
      <li class="services__item"><span class="services__bullet"></span>Snow Plowing</li>
      <li class="services__item"><span class="services__bullet"></span>Snow Blowing</li>
      <li class="services__item"><span class="services__bullet"></span>Snow Shoveling</li>
      <li class="services__item"><span class="services__bullet"></span>Ice Removal</li>
      <li class="services__item"><span class="services__bullet"></span>Salting/Sanding</li>
    </ul>
  </section>

  <div class="credentials">
    <p class="credentials__line">Fully Licensed and Insured</p>
    <p class="credentials__hours">Available and ON CALL 24/7</p>
  </div>

  <div class="reserve">
    <p>CALL NOW TO RESERVE</p>
    <p>XX XXXX XX XXX</p>
  </div>
</main>
</body>
</html>
```